business card for a shoe shop

we would like a business card for a family owned shoe shop.
With this information included.
Darnell's Shoe Store
Family owned since 1947

then on other side
Darnell's Shoe Store
Footwear fitting specialist
Phone: 9187 2630
218 Quarry St, Fernleigh Downs 3187
(cnr. Hartwick Rd and Quarry St)
darnellshoes218@examplemail.com
if could incorporate the purple color on card i have attached.

```html
<!DOCTYPE html>
<html lang="en">
<head>
<meta charset="utf-8">
<title>Darnell's Shoe Store — Business Card</title>
<link href="https://fonts.googleapis.com/css2?family=Abril+Fatface&family=Poppins:wght@300;400&display=swap" rel="stylesheet">
<style>
  :root {
    --brand-purple: #977ab5;
    --card-white: #f7f7f8;
    --panel-grey: #ececee;
    --ink: #2e2e33;
    --canvas-bg: #e9e9ea;
  }
  * { box-sizing: border-box; margin: 0; padding: 0; }
  html, body {
    width: 1200px;
    height: 900px;
    overflow: hidden;
    background: var(--canvas-bg);
  }
  .canvas {
    width: 1200px;
    height: 900px;
    display: flex;
    flex-direction: column;
    align-items: center;
    justify-content: center;
    gap: 56px;
  }
  .card {
    width: 560px;
    height: 320px;
    position: relative;
    box-shadow: 0 10px 28px rgba(0, 0, 0, 0.12);
  }
  .brand-name {
    font-family: "Abril Fatface", serif;
    font-weight: 400;
    letter-spacing: 0.2px;
  }

  /* Front side */
  .card--front {
    background: var(--brand-purple);
    color: #ffffff;
    display: flex;
    flex-direction: column;
    align-items: center;
    justify-content: center;
  }
  .card--front .brand-name { font-size: 40px; line-height: 1; }
  .card--front .tagline {
    font-family: "Poppins", sans-serif;
    font-weight: 300;
    font-size: 16px;
    margin-top: 10px;
    letter-spacing: 0.3px;
  }

  /* Back side */
  .card--back {
    background: var(--card-white);
    padding: 16px;
  }
  .back-panel {
    position: relative;
    width: 100%;
    height: 100%;
    background: var(--panel-grey);
    display: flex;
    flex-direction: column;
    align-items: center;
    justify-content: center;
    text-align: center;
    color: var(--ink);
  }
  .corner-mark {
    position: absolute;
    width: 46px;
    height: 78px;
  }
  .corner-mark--bottom-left { left: 0; bottom: 0; }
  .corner-mark--top-right { right: 0; top: 0; }
  .corner-mark polygon { fill: var(--brand-purple); }
  .card--back .brand-name {
    font-size: 31px;
    line-height: 1;
    color: var(--brand-purple);
  }
  .card--back .specialty {
    font-family: "Poppins", sans-serif;
    font-weight: 400;
    font-size: 13px;
    margin-top: 6px;
  }
  .divider {
    width: 56px;
    height: 2px;
    background: var(--brand-purple);
    margin: 16px 0 16px;
  }
  .contact-list {
    list-style: none;
    font-family: "Poppins", sans-serif;
    font-weight: 400;
    font-size: 13px;
    line-height: 1.55;
  }
</style>
</head>
<body>
  <main class="canvas">
    <section class="card card--front" aria-label="Card front">
      <h1 class="brand-name">Darnell's Shoe Store</h1>
      <p class="tagline">Family Owned Since 1947</p>
    </section>

    <section class="card card--back" aria-label="Card back">
      <div class="back-panel">
        <svg class="corner-mark corner-mark--bottom-left" viewBox="0 0 46 78" aria-hidden="true">
          <polygon points="0,0 46,78 0,78"/>
        </svg>
        <svg class="corner-mark corner-mark--top-right" viewBox="0 0 46 78" aria-hidden="true">
          <polygon points="0,0 46,0 46,78"/>
        </svg>

        <h2 class="brand-name">Darnell's Shoe Store</h2>
        <p class="specialty">Footwear fitting specialist</p>
        <div class="divider"></div>
        <ul class="contact-list">
          <li>Phone: 9187 2630</li>
          <li>218 Quarry St, Fernleigh Downs 3187</li>
          <li>(cnr. Hartwick Rd and Quarry St)</li>
          <li>darnellshoes218@examplemail.com</li>
        </ul>
      </div>
    </section>
  </main>
</body>
</html>
```